Oil Field Service company needs professional business cards

Looking to clean up our current company business cards and look a little more professional. Harlow Tubular Services is a US based company that services the oil field. We deal with engineers, managers and oil rigs....................................................................................................................................................................................................................................................................................................................................................................................................

Target Market(s)

Oil and Gas professionals

Industry/Entity Type

Oil And Gas

Contact Information for Business Card

See attached photo as example

Font styles to use
Sans Serif

Colors
ec1f27

Requirements
Must have
• Company Logo, Name, Title, Cell, Office, Fax, Email.
• See attached photo
Nice to have
• External CRT, Internal CRT, Casing Crews, Torque Turn, Laydown Machine
Should not have
• Do not introduce any new pictures and keep it professional looking

```html
<!DOCTYPE html>
<html lang="en">
<head>
<meta charset="utf-8">
<title>Harlow Tubular Services – Business Card</title>
<link rel="stylesheet" href="https://fonts.googleapis.com/css2?family=Open+Sans:wght@400;600;700&display=swap">
<style>
  :root {
    --brand-red: #e31b23;
    --slate: #3f4a53;
    --text-grey: #4a4f55;
    --rule-grey: #8a8f94;
    --card-white: #fbfbfa;
    --page-bg: #e9e9e9;
  }
  * { box-sizing: border-box; margin: 0; padding: 0; }
  html, body {
    width: 1105px; height: 1200px; overflow: hidden;
    background: var(--page-bg);
    font-family: "Open Sans", Arial, sans-serif;
  }
  .card {
    position: absolute; left: 196px;
    width: 720px; height: 410px;
    overflow: hidden;
  }
  .card-front { top: 146px; background: var(--card-white); }
  .card-back { top: 602px; background: var(--brand-red); color: #fff; }

  .front-wordmark {
    position: absolute; right: 36px; top: 62px;
    text-align: right;
    color: var(--slate);
    font-weight: 700; font-size: 34px; line-height: 1.1;
    letter-spacing: 0.5px;
  }
  .holder-name {
    position: absolute; left: 33px; top: 190px;
    color: var(--brand-red); font-weight: 600; font-size: 26px;
  }
  .holder-title {
    position: absolute; left: 33px; top: 223px;
    color: var(--text-grey); font-size: 19px;
  }
  .divider {
    position: absolute; left: 33px; right: 36px; top: 257px;
    height: 1px; background: var(--rule-grey);
  }
  .contact-list {
    position: absolute; left: 33px; top: 269px; list-style: none;
  }
  .contact-list li {
    display: flex; align-items: center;
    height: 27.5px; color: var(--text-grey); font-size: 19px;
  }
  .contact-list svg { width: 20px; height: 20px; margin-right: 12px; fill: var(--brand-red); }
  .address-block {
    position: absolute; right: 36px; top: 323px;
    text-align: right; color: var(--text-grey); font-size: 19px; line-height: 26px;
  }
  .edge-band { position: absolute; left: 0; bottom: 0; width: 720px; height: 10px; }

  .back-wordmark {
    position: absolute; left: 0; right: 0; top: 160px;
    text-align: center; font-weight: 700; font-size: 42px; letter-spacing: 0.5px;
  }
  .service-list {
    position: absolute; left: 0; right: 0; top: 320px;
    text-align: center; font-size: 19px; line-height: 27px;
  }
</style>
</head>
<body>

<section class="card card-front">
  <div class="front-wordmark">Harlow Tubular<br>Services</div>
  <h1 class="holder-name">Wade Kessler</h1>
  <p class="holder-title">Area Manager</p>
  <div class="divider"></div>
  <ul class="contact-list">
    <li><svg viewBox="0 0 24 24"><path d="M6.6 10.8a15 15 0 0 0 6.6 6.6l2.2-2.2c.3-.3.7-.4 1-.2 1.1.4 2.3.6 3.6.6.6 0 1 .4 1 1V20c0 .6-.4 1-1 1A17 17 0 0 1 3 4c0-.6.4-1 1-1h3.5c.6 0 1 .4 1 1 0 1.3.2 2.5.6 3.6.1.3 0 .7-.2 1z"/></svg>(555)214-6800</li>
    <li><svg viewBox="0 0 24 24"><path d="M7 1h10a2 2 0 0 1 2 2v18a2 2 0 0 1-2 2H7a2 2 0 0 1-2-2V3a2 2 0 0 1 2-2zm0 3v14h10V4zm5 15.5a1.2 1.2 0 1 0 0 2.4 1.2 1.2 0 0 0 0-2.4z"/></svg>(555)387-2914</li>
    <li><svg viewBox="0 0 24 24"><path d="M6 2h10l2 2v5H6zM3 10h18a2 2 0 0 1 2 2v8H1v-8a2 2 0 0 1 2-2zm2 4v2h6v-2zm-2 7h18v1H3z"/></svg>(555)214-6830</li>
    <li><svg viewBox="0 0 24 24"><path d="M2 5h20v2l-10 6L2 7zm0 4.3 10 6 10-6V19H2z"/></svg>wade@harlowtubular.com</li>
  </ul>
  <div class="address-block">
    <p>Alder Springs, OK 73000</p>
    <p>www.harlowtubular.com</p>
  </div>
  <svg class="edge-band" viewBox="0 0 720 10" preserveAspectRatio="none">
    <polygon points="0,0 474,0 471,10 0,10" fill="var(--slate)"/>
    <polygon points="478,0 720,0 720,10 475,10" fill="var(--brand-red)"/>
  </svg>
</section>

<section class="card card-back">
  <div class="back-wordmark">Harlow Tubular Services</div>
  <div class="service-list">
    <p>External CRT &nbsp;|&nbsp; Internal CRT &nbsp;|&nbsp; Casing Crews</p>
    <p>Torque Turn &nbsp;|&nbsp; Laydown Machine</p>
  </div>
</section>

</body>
</html>
```